Simple elegant feminine design - Going out on my own as a Mortgage Broker.
My thoughts are the following details on the Front, middle of the card possibly? Phone and email smaller font than my name?
Marnie Veltrin
Finance Specialist
p: 0438 215 962
e: marnie@veltrinlending.com.au
Bottom of the card
residential / commercial / equipment
I would like the Font in Rose Gold maybe white or black background? or Possibly a stone grey - are you able to do a few options? I'd like them embossed
Then I had an idea as a simple logo as per the attached if you get the idea in my scribble, my initials, capital M attached to a small v that leads/follows into a circle? Thicker Font In Rose Gold, middle of the card at the back.
Very open to ideas though and what colour you think would look better with the Rose Gold.
Thanks so much for your help, I am not very creative and savvy with this stuff :-)
Industry/Entity Type
Finance
Contact Information for Business Card
Marnie Veltrin
p: 0438 215 962
Look and feel

```html
<!DOCTYPE html>
<html lang="en">
<head>
<meta charset="utf-8">
<title>Marnie's Business Cards</title>
<link rel="stylesheet" href="https://fonts.googleapis.com/css2?family=Montserrat:wght@400;500;600&display=swap">
<style>
  :root {
    --backdrop: #e9ebee;
    --card: #e9eaed;
    --card-edge: #dcdee2;
    --rose: #b36a77;
  }
  html, body {
    margin: 0;
    padding: 0;
    width: 1200px;
    height: 1200px;
    overflow: hidden;
    background: var(--backdrop);
    font-family: "Montserrat", Arial, sans-serif;
    color: var(--rose);
  }
  .sheet {
    position: relative;
    width: 1200px;
    height: 1200px;
  }
  .card {
    position: absolute;
    left: 246px;
    width: 700px;
    height: 400px;
    background: var(--card);
    border: 1px solid var(--card-edge);
    box-sizing: border-box;
  }
  .card--front { top: 146px; }
  .card--back  { top: 652px; }

  .brand {
    position: absolute;
    inset: 0;
    display: flex;
    align-items: center;
    justify-content: center;
    gap: 18px;
  }
  .brand-dot {
    width: 18px;
    height: 18px;
    border-radius: 50%;
    background: var(--rose);
  }
  .brand-name {
    font-size: 34px;
    font-weight: 500;
    letter-spacing: 6px;
    text-transform: uppercase;
  }

  .identity {
    position: absolute;
    top: 104px;
    left: 0;
    right: 0;
    text-align: center;
  }
  .person-name {
    margin: 0;
    font-size: 31px;
    font-weight: 600;
    letter-spacing: 5px;
    text-transform: uppercase;
    line-height: 1;
  }
  .person-role {
    margin: 12px 0 0;
    font-size: 22px;
    font-weight: 400;
    letter-spacing: 1px;
    text-transform: uppercase;
    line-height: 1;
  }
  .contact {
    list-style: none;
    margin: 44px 0 0;
    padding: 0;
    font-size: 24px;
    line-height: 30px;
  }
  .contact-item {
    display: flex;
    align-items: center;
    justify-content: center;
    gap: 8px;
  }
  .contact-icon {
    width: 22px;
    height: 22px;
    fill: var(--rose);
  }
  .services {
    position: absolute;
    bottom: 22px;
    left: 0;
    right: 0;
    margin: 0;
    text-align: center;
    font-size: 20px;
    letter-spacing: 3.6px;
    text-transform: uppercase;
  }
</style>
</head>
<body>
<main class="sheet">
  <section class="card card--front" aria-label="Card front">
    <div class="brand">
      <span class="brand-dot" aria-hidden="true"></span>
      <span class="brand-name">Marnie Veltrin</span>
    </div>
  </section>

  <section class="card card--back" aria-label="Card back">
    <div class="identity">
      <h1 class="person-name">Marnie Veltrin</h1>
      <p class="person-role">Finance Specialist</p>
      <ul class="contact">
        <li class="contact-item">
          <svg class="contact-icon" viewBox="0 0 24 24" aria-hidden="true">
            <path d="M6.6 10.8c1.4 2.8 3.8 5.1 6.6 6.6l2.2-2.2c.3-.3.7-.4 1-.2 1.1.4 2.3.6 3.6.6.6 0 1 .4 1 1V20c0 .6-.4 1-1 1C10.6 21 3 13.4 3 4c0-.6.4-1 1-1h3.5c.6 0 1 .4 1 1 0 1.3.2 2.5.6 3.6.1.3 0 .7-.2 1l-2.3 2.2z"/>
          </svg>
          <span>0438 215 962</span>
        </li>
        <li class="contact-item">
          <svg class="contact-icon" viewBox="0 0 24 24" aria-hidden="true">
            <path d="M2 5h20v14H2z M3.5 6.5 12 12.5l8.5-6" fill="var(--rose)"/>
            <path d="M3 6l9 6.5L21 6" fill="none" stroke="var(--card)" stroke-width="1.6"/>
          </svg>
          <span>marnie@veltrinlending.com.au</span>
        </li>
      </ul>
    </div>
    <p class="services">Residential / Commercial / Equipment</p>
  </section>
</main>
</body>
</html>
```